Bluebird Business Card Design

Name Marlene Obadofor
Title Mortgage Originator
Office (800) 416-2795 x65
Direct (240) 615-2079
Email mobadofor@bluebirdlending.example
NMLS 3817465
Licensed MD

Name Dorian Pelletier
Title Mortgage Originator
Office (800) 416-2795 x66
Direct (404) 263-5147
Email dpelletier@bluebirdlending.example
NMLS 3156702
Licensed MD

Name Rochelle Barnaby
Title Mortgage Originator
Office (800) 416-2795 x67
Direct (443) 812-3659
Email barnabyrochelle@mailpost.example
NMLS 3902576
Licensed MD

Name Omar Teldouri
Title Mortgage Originator
Office (800) 416-2795 x32
Direct (571) 326-7045
Email oteldouri@bluebirdlending.example
NMLS 1573064
Licensed MD

```html
<!DOCTYPE html>
<html lang="en">
<head>
<meta charset="utf-8">
<title>Bluebird Business Cards</title>
<link rel="stylesheet" href="https://fonts.googleapis.com/css2?family=Barlow+Semi+Condensed:wght@400;500&display=swap">
<style>
  :root {
    --page-bg: #e6e7e9;
    --card-bg: #ffffff;
    --card-edge: #d3d5d8;
    --brand-blue: #1f75c0;
    --brand-navy: #0d4a80;
    --ink: #1d1d1f;
  }
  html, body {
    margin: 0;
    width: 1200px;
    height: 1200px;
    overflow: hidden;
    background: var(--page-bg);
    font-family: "Barlow Semi Condensed", sans-serif;
  }
  .card-sheet { position: relative; width: 1200px; height: 1200px; }
  .card {
    position: absolute;
    width: 381px;
    height: 218px;
    background: var(--card-bg);
    border: 1px solid var(--card-edge);
    border-radius: 12px;
    overflow: hidden;
    box-sizing: border-box;
  }
  .card--a { left: 214px; top: 352px; }
  .card--b { left: 624px; top: 352px; }
  .card--c { left: 214px; top: 597px; }
  .card--d { left: 624px; top: 597px; }
  .card__band {
    position: absolute; left: 0; top: 0;
    width: 135px; height: 100%;
    background: var(--brand-blue);
  }
  .card__portrait {
    position: absolute; left: 23px; top: 27px;
    width: 122px; height: 164px;
  }
  .portrait--warm { background: linear-gradient(160deg, #8a6b52, #4a3a30 60%, #6d5a3e); }
  .portrait--dark { background: linear-gradient(160deg, #2b2b2e, #1c2238 60%, #2a2f45); }
  .portrait--light { background: linear-gradient(160deg, #f3f1ef, #d9b8a2 60%, #efe6df); }
  .portrait--grey { background: linear-gradient(160deg, #e4e2df, #a9ada5 60%, #d8d6d2); }
  .card__brand {
    position: absolute; right: 22px; top: 14px;
    display: flex; align-items: center; gap: 5px;
    color: var(--brand-navy);
    font-weight: 500;
    font-size: 17px;
  }
  .card__brand-dot {
    width: 12px; height: 12px; border-radius: 50%;
    background: var(--brand-navy);
  }
  .card__info {
    position: absolute; left: 168px; top: 58px;
    color: var(--ink);
  }
  .card__name {
    margin: 0;
    font-size: 23px;
    font-weight: 500;
    color: var(--brand-blue);
    line-height: 26px;
  }
  .card__title { margin: 0 0 20px; font-size: 13.5px; line-height: 16px; }
  .card__contacts { margin: 0; padding: 0; list-style: none; font-size: 13px; line-height: 16.5px; white-space: nowrap; }
  .card__contacts .email { font-size: 12.2px; }
</style>
</head>
<body>
<main class="card-sheet">

  <article class="card card--a">
    <div class="card__band"></div>
    <div class="card__portrait portrait--warm" role="img" aria-label="Portrait photo of Marlene Obadofor"></div>
    <div class="card__brand"><span class="card__brand-dot"></span>Bluebird</div>
    <div class="card__info">
      <h2 class="card__name">Marlene Obadofor</h2>
      <p class="card__title">Mortgage Originator</p>
      <ul class="card__contacts">
        <li>Office (800) 416-2795 x65</li>
        <li>Direct (240) 615-2079</li>
        <li class="email">Email mobadofor@bluebirdlending.example</li>
        <li>NMLS 3817465</li>
        <li>Licensed MD</li>
      </ul>
    </div>
  </article>

  <article class="card card--b">
    <div class="card__band"></div>
    <div class="card__portrait portrait--dark" role="img" aria-label="Portrait photo of Dorian Pelletier"></div>
    <div class="card__brand"><span class="card__brand-dot"></span>Bluebird</div>
    <div class="card__info">
      <h2 class="card__name">Dorian Pelletier</h2>
      <p class="card__title">Mortgage Originator</p>
      <ul class="card__contacts">
        <li>Office (800) 416-2795 x66</li>
        <li>Direct (404) 263-5147</li>
        <li class="email">Email dpelletier@bluebirdlending.example</li>
        <li>NMLS 3156702</li>
        <li>Licensed MD</li>
      </ul>
    </div>
  </article>

  <article class="card card--c">
    <div class="card__band"></div>
    <div class="card__portrait portrait--light" role="img" aria-label="Portrait photo of Rochelle Barnaby"></div>
    <div class="card__brand"><span class="card__brand-dot"></span>Bluebird</div>
    <div class="card__info">
      <h2 class="card__name">Rochelle Barnaby</h2>
      <p class="card__title">Mortgage Originator</p>
      <ul class="card__contacts">
        <li>Office (800) 416-2795 x67</li>
        <li>Direct (443) 812-3659</li>
        <li class="email">Email barnabyrochelle@mailpost.example</li>
        <li>NMLS 3902576</li>
        <li>Licensed MD</li>
      </ul>
    </div>
  </article>

  <article class="card card--d">
    <div class="card__band"></div>
    <div class="card__portrait portrait--grey" role="img" aria-label="Portrait photo of Omar Teldouri"></div>
    <div class="card__brand"><span class="card__brand-dot"></span>Bluebird</div>
    <div class="card__info">
      <h2 class="card__name">Omar Teldouri</h2>
      <p class="card__title">Mortgage Originator</p>
      <ul class="card__contacts">
        <li>Office (800) 416-2795 x32</li>
        <li>Direct (571) 326-7045</li>
        <li class="email">Email oteldouri@bluebirdlending.example</li>
        <li>NMLS 1573064</li>
        <li>Licensed MD</li>
      </ul>
    </div>
  </article>

</main>
</body>
</html>
```